Create a book cover for velmora QPL

We are looking for a designer to design a cover for a log book in two versions. The two versions only have a slight difference in page count and text, other than that, it is one design.

The main color is blue. No black, no white except book title and other text. The cover must closely relate to the interior pages provided in the attachment. The style should be simple and modern, no old school graphics and fonts. Apply color psychology in the design. Please be creative and you are allowed to use download templates and graphic elements, but you must provide commercial licenses.

Here are the basic information of the book:
1. Book title: MOTOR CARE TRACKER JOURNAL
2. Book size: 6x9 inches
3. Page count: 61 (version 1) and 73 (version 2)
4. Platform: velmora qpl

Requirement for version 1:
1. Front cover: book title
2. Spine: no book title and author name
3. Back cover: text on the top and pen name logo on the bottom middle
4. Back cover text:
• Your essential tool for tracking vehicle health and maintenance
• Dedicated sections for maintenance schedules and repair history
• Track up to 30 maintenance schedules and repair history
• Easy-to-use tables and clear layouts
• Perfect for all car owners, from enthusiasts to everyday drivers

We hope it helps you keep your vehicle in excellent condition. Please take a moment to leave a positive review on Velmora and share your experience if you find it helpful. Thank you!

Requirement for version 2:
1. Front cover: book title ,text "COLOR PAGES"
4. Back cover text:
• Track up to 36 maintenance schedules and repair history

Export:
1. Cover design in PDF and editable file format.
2. Sources/Commercial licenses for everything you did not create by yourself including fonts.

```html
<!DOCTYPE html>
<html lang="en">
<head>
<meta charset="utf-8">
<title>Motor Care Tracker Journal – Cover Spread</title>
<link rel="stylesheet" href="https://fonts.googleapis.com/css2?family=Red+Hat+Display:wght@300;400;500;800&display=swap">
<style>
  :root {
    --navy: #212f6e;
    --navy-deep: #0a1838;
    --midnight: #050d22;
    --cyan: #27c6ec;
    --ice: #c9eef7;
    --teal: #4fa6c2;
    --text: #ffffff;
    --page: #ffffff;
  }
  * { box-sizing: border-box; margin: 0; padding: 0; }
  html, body { width: 1200px; height: 1200px; overflow: hidden; background: var(--page); }
  body { position: relative; font-family: "Red Hat Display", Arial, sans-serif; color: var(--text); }

  .cover-spread {
    position: absolute; left: 80px; top: 225px;
    width: 1040px; height: 750px; overflow: hidden;
    background: var(--navy);
  }
  .cover-art { position: absolute; inset: 0; width: 100%; height: 100%; }

  .back-cover { position: absolute; left: 81px; top: 66px; width: 400px; }
  .title-small { font-weight: 800; font-size: 32px; line-height: 34px; letter-spacing: 0.2px; }
  .title-small .accent, .title-large .accent { font-weight: 300; color: var(--cyan); }

  .feature-list { list-style: none; margin-top: 26px; width: 350px; }
  .feature-list li {
    position: relative; padding-left: 28px; font-size: 14px; line-height: 17px;
    font-weight: 500; margin-bottom: 11px;
  }
  .feature-list svg { position: absolute; left: 0; top: 0; width: 18px; height: 18px; }

  .pen-name {
    position: absolute; left: 252px; top: 637px; transform: translate(-50%, -50%);
    display: flex; align-items: center; gap: 10px; white-space: nowrap;
    font-size: 18px; font-weight: 500; letter-spacing: 1px;
  }
  .pen-name .dot { width: 14px; height: 14px; border-radius: 50%; background: var(--ice); }

  .front-cover { position: absolute; left: 584px; top: 182px; }
  .title-large { font-weight: 800; font-size: 55px; line-height: 55px; letter-spacing: 0.3px; }
  .title-large .accent { font-size: 50px; line-height: 58px; }

  .car-illustration {
    position: absolute; left: 584px; top: 380px; width: 300px; height: 70px;
    border-radius: 40px 70px 12px 12px;
    background: linear-gradient(180deg, rgba(79,166,194,0.22), rgba(33,47,110,0.05));
  }
</style>
</head>
<body>
<main class="cover-spread">
  <svg class="cover-art" viewBox="0 0 1224 883" preserveAspectRatio="none" aria-hidden="true">
    <defs>
      <linearGradient id="bg-fade" x1="0" y1="0" x2="0" y2="1">
        <stop offset="0" stop-color="#222f6e"/>
        <stop offset="0.3" stop-color="#1b2a60"/>
        <stop offset="0.62" stop-color="#071430"/>
        <stop offset="0.78" stop-color="#12235a"/>
        <stop offset="1" stop-color="#212f6e"/>
      </linearGradient>
      <radialGradient id="left-shadow" cx="0.05" cy="0.6" r="0.35">
        <stop offset="0" stop-color="#02060f" stop-opacity="0.9"/>
        <stop offset="1" stop-color="#02060f" stop-opacity="0"/>
      </radialGradient>
      <radialGradient id="glow" cx="0.5" cy="0.5" r="0.5">
        <stop offset="0" stop-color="#e8fbff" stop-opacity="0.9"/>
        <stop offset="0.4" stop-color="#4fc3e0" stop-opacity="0.5"/>
        <stop offset="1" stop-color="#4fc3e0" stop-opacity="0"/>
      </radialGradient>
      <linearGradient id="band" x1="0" y1="0" x2="1" y2="0">
        <stop offset="0" stop-color="#4fa6c2"/>
        <stop offset="0.25" stop-color="#f2fdff"/>
        <stop offset="0.55" stop-color="#7cc7dc"/>
        <stop offset="1" stop-color="#2f7ea3"/>
      </linearGradient>
      <linearGradient id="band-dark" x1="0" y1="0" x2="1" y2="0">
        <stop offset="0" stop-color="#1c6a8c"/>
        <stop offset="1" stop-color="#6fb8d4"/>
      </linearGradient>
    </defs>
    <rect width="1224" height="883" fill="url(#bg-fade)"/>
    <rect width="1224" height="883" fill="url(#left-shadow)"/>
    <ellipse cx="300" cy="535" rx="420" ry="28" fill="url(#glow)"/>
    <polygon points="985,705 1224,455 1224,883 1060,883" fill="#0a1838" opacity="0.55"/>
    <path d="M0,575 L630,575 L745,718 L985,718 L1224,418" fill="none" stroke="url(#band)" stroke-width="20" stroke-linejoin="round"/>
    <path d="M0,622 L640,622 L760,740 L1000,740 L1224,480" fill="none" stroke="url(#band-dark)" stroke-width="5" opacity="0.8"/>
    <path d="M0,545 L1224,545" stroke="#8fd8ee" stroke-width="3" opacity="0.6"/>
    <path d="M920,883 L1224,470" stroke="#3b8bb3" stroke-width="2" opacity="0.5"/>
  </svg>

  <section class="back-cover">
    <h2 class="title-small">MOTOR CARE<br>TRACKER<br><span class="accent">JOURNAL</span></h2>
    <ul class="feature-list">
      <li><svg viewBox="0 0 20 20"><circle cx="10" cy="10" r="8" fill="none" stroke="#27c6ec" stroke-width="2"/><circle cx="10" cy="11" r="2.2" fill="#27c6ec"/><path d="M3 9 Q10 6 17 9 M10 13 V18" stroke="#27c6ec" stroke-width="2" fill="none"/></svg>Your essential tool for tracking vehicle health and maintenance</li>
      <li><svg viewBox="0 0 20 20"><circle cx="10" cy="10" r="8" fill="none" stroke="#27c6ec" stroke-width="2"/><circle cx="10" cy="11" r="2.2" fill="#27c6ec"/><path d="M3 9 Q10 6 17 9 M10 13 V18" stroke="#27c6ec" stroke-width="2" fill="none"/></svg>Dedicated sections for maintenance schedules and repair history</li>
      <li><svg viewBox="0 0 20 20"><circle cx="10" cy="10" r="8" fill="none" stroke="#27c6ec" stroke-width="2"/><circle cx="10" cy="11" r="2.2" fill="#27c6ec"/><path d="M3 9 Q10 6 17 9 M10 13 V18" stroke="#27c6ec" stroke-width="2" fill="none"/></svg>Track up to 30 maintenance schedules and<br>repair history</li>
      <li><svg viewBox="0 0 20 20"><circle cx="10" cy="10" r="8" fill="none" stroke="#27c6ec" stroke-width="2"/><circle cx="10" cy="11" r="2.2" fill="#27c6ec"/><path d="M3 9 Q10 6 17 9 M10 13 V18" stroke="#27c6ec" stroke-width="2" fill="none"/></svg>Easy-to-use tables and clear layouts</li>
      <li><svg viewBox="0 0 20 20"><circle cx="10" cy="10" r="8" fill="none" stroke="#27c6ec" stroke-width="2"/><circle cx="10" cy="11" r="2.2" fill="#27c6ec"/><path d="M3 9 Q10 6 17 9 M10 13 V18" stroke="#27c6ec" stroke-width="2" fill="none"/></svg>Perfect for all car owners, from enthusiasts to everyday drivers</li>
    </ul>
  </section>

  <div class="pen-name"><span class="dot"></span>DORIAN HALE</div>

  <section class="front-cover">
    <h1 class="title-large">MOTOR CARE<br>TRACKER<br><span class="accent">JOURNAL</span></h1>
  </section>

  <div class="car-illustration" role="img" aria-label="Faint outline of a sports car in glowing blue lines"></div>
</main>
</body>
</html>
```